Construction Company

Design a clutter free business card, it can be double-sided utilizing the logo for BDN Ltd simple with all relevant contact information.

Please also a letterhead design to function for the purposes of invoicing, all mail requirements, with header to be distinctive while the footer ties page together and incorporates all necessary information.

For now, please use generic / dummy text and when a winner is selected, I will disclose the contact information.

Hi Designers! Please read the updated brief which includes the design of a business card and letterhead. Thank you!

```html
<!DOCTYPE html>
<html lang="en">
<head>
<meta charset="utf-8">
<title>BDN Ltd — Business Card Concepts</title>
<link href="https://fonts.googleapis.com/css2?family=Playfair+Display:wght@400;700&family=Roboto:wght@400;500;700&display=swap" rel="stylesheet">
<style>
  :root {
    --navy: #0a318f;
    --gold: #b8901e;
    --ink: #1d1d1d;
    --board: #eceeee;
    --paper: #ffffff;
    --faint: #f3f3f3;
    --sans: "Roboto", Arial, sans-serif;
    --serif: "Playfair Display", Georgia, serif;
  }
  * { box-sizing: border-box; margin: 0; padding: 0; }
  html, body { width: 1008px; height: 1200px; overflow: hidden; }
  body { background: var(--board); font-family: var(--sans); color: var(--ink); position: relative; }

  .card { position: absolute; width: 432px; height: 249px; background: var(--paper); overflow: hidden; }
  .col-left { left: 60px; }
  .col-right { left: 516px; }
  .row-1 { top: 64px; }
  .row-2 { top: 338px; }
  .row-3 { top: 611px; }
  .row-4 { top: 885px; }
  .card--navy { background: var(--navy); }

  .wordmark { position: absolute; font-family: var(--serif); font-weight: 700; color: var(--navy); white-space: nowrap; line-height: 1; letter-spacing: -0.5px; }

  .decor-faint { position: absolute; left: 0; top: 0; width: 190px; height: 100%;
    background: linear-gradient(90deg, var(--faint), #f7f7f7 70%, var(--paper)); }
  .decor-pattern { position: absolute; inset: 0;
    background: radial-gradient(circle at 50% 50%, #ffffff 0, #f6f6f6 45%, #efefef 100%); }

  .person-name { position: absolute; white-space: nowrap; }
  .person-role { position: absolute; white-space: nowrap; }
  .contact-list { position: absolute; list-style: none; }
  .contact-list li { display: flex; align-items: center; gap: 6px; white-space: nowrap; }
  .contact-list svg { flex: none; }
  .rule { position: absolute; height: 2px; width: 26px; background: var(--ink); }

  /* card 2 — minimal sans */
  .c2 .person-name { left: 37px; top: 124px; font-size: 15px; }
  .c2 .person-role { left: 37px; top: 143px; font-size: 9.5px; }
  .c2 .rule { left: 37px; top: 160px; }
  .c2 .contact-list { left: 37px; top: 173px; font-size: 11.5px; }
  .c2 .contact-list li { height: 16px; }

  /* card 4 — classic serif */
  .c4 .person-name { left: 30px; top: 128px; font-family: var(--serif); font-weight: 700; font-size: 15px; color: var(--navy); letter-spacing: 0.6px; }
  .c4 .person-role { left: 30px; top: 149px; font-family: var(--serif); font-size: 8px; color: var(--gold); letter-spacing: 0.6px; }
  .c4 .contact-list { top: 172px; font-family: var(--serif); font-size: 13px; color: var(--navy); }
  .c4 .contact-list li { height: 17.5px; }
  .c4 .contact-list.left { left: 30px; }
  .c4 .contact-list.right { left: 244px; }
  .c4 .web { color: var(--gold); }

  /* card 6 — logo and contact with mark */
  .c6 .person-name { left: 37px; top: 102px; font-weight: 700; font-size: 13px; color: var(--navy); }
  .c6 .person-role { left: 37px; top: 118px; font-size: 10px; color: var(--gold); }
  .c6 .address { position: absolute; left: 37px; top: 139px; font-size: 10px; line-height: 13.5px; color: var(--navy); }
  .c6 .contact-list { left: 37px; top: 172px; font-size: 12px; color: var(--navy); }
  .c6 .contact-list li { height: 16px; }
  .mark-dot { position: absolute; border-radius: 50%; background: var(--gold); }
</style>
</head>
<body>

<!-- Card 1: front with faint side decoration -->
<section class="card col-left row-1 c1">
  <div class="decor-faint" role="img" aria-label="Faint large brand emblem decoration"></div>
  <span class="wordmark" style="left:268px; top:174px; font-size:34px;">BDN Ltd</span>
</section>

<!-- Card 2: back, minimal -->
<section class="card col-right row-1 c2">
  <span class="wordmark" style="left:272px; top:44px; font-size:32px;">BDN Ltd</span>
  <p class="person-name">Daniel Harwood</p>
  <p class="person-role">Managing Director</p>
  <span class="rule"></span>
  <ul class="contact-list">
    <li><svg width="9" height="10" viewBox="0 0 9 10"><rect x="2" y="0.5" width="5" height="9" rx="1" fill="none" stroke="#1d1d1d" stroke-width="1.2"/><rect x="3.8" y="7.4" width="1.4" height="1" fill="#1d1d1d"/></svg>555 555 55 55</li>
    <li><svg width="9" height="10" viewBox="0 0 9 10"><rect x="0.5" y="2" width="8" height="6" fill="#1d1d1d"/><path d="M0.5 2 L4.5 5.5 L8.5 2" fill="none" stroke="#fff" stroke-width="1"/></svg>d.harwood@bdn-ltd.com</li>
    <li><svg width="9" height="10" viewBox="0 0 10 10"><circle cx="5" cy="5" r="4.2" fill="none" stroke="#1d1d1d" stroke-width="1"/><ellipse cx="5" cy="5" rx="1.8" ry="4.2" fill="none" stroke="#1d1d1d" stroke-width="0.8"/><path d="M0.8 5 H9.2" stroke="#1d1d1d" stroke-width="0.8"/></svg>www.bdn-ltd.com</li>
  </ul>
</section>

<!-- Card 3: centered name -->
<section class="card col-left row-2 c3">
  <span class="wordmark" style="left:0; width:432px; text-align:center; top:100px; font-size:48px;">BDN Ltd</span>
</section>

<!-- Card 4: serif contact side -->
<section class="card col-right row-2 c4">
  <span class="wordmark" style="left:250px; top:46px; font-size:36px;">BDN Ltd</span>
  <p class="person-name">DANIEL HARWOOD</p>
  <p class="person-role">MANAGING DIRECTOR</p>
  <ul class="contact-list left">
    <li><svg width="10" height="10" viewBox="0 0 10 10"><rect x="0.5" y="0.5" width="9" height="9" rx="2" fill="none" stroke="#b8901e"/><rect x="3.5" y="2.5" width="3" height="5" rx="0.5" fill="none" stroke="#b8901e" stroke-width="0.8"/></svg>555 555 55 55</li>
    <li><svg width="10" height="10" viewBox="0 0 10 10"><rect x="0.5" y="0.5" width="9" height="9" rx="2" fill="none" stroke="#b8901e"/><rect x="2.5" y="3.5" width="5" height="3" rx="1" fill="#b8901e"/></svg>888 888 88 88</li>
    <li><svg width="10" height="10" viewBox="0 0 10 10"><rect x="0.5" y="0.5" width="9" height="9" rx="2" fill="none" stroke="#b8901e"/><rect x="2.5" y="3" width="5" height="4" fill="#b8901e"/></svg>d.harwood@bdn-ltd.com</li>
  </ul>
  <ul class="contact-list right">
    <li>123 Fake Street</li>
    <li>Anytown, New York 12345</li>
    <li class="web">www.bdn-ltd.com</li>
  </ul>
</section>

<!-- Card 5: patterned front -->
<section class="card col-left row-3 c5">
  <div class="decor-pattern" role="img" aria-label="Fine radiating line pattern in light grey"></div>
  <span class="wordmark" style="left:0; width:432px; text-align:center; top:106px; font-size:38px; color:var(--gold);">BDN Ltd</span>
</section>

<!-- Card 6: contact side with mark -->
<section class="card col-right row-3 c6">
  <span class="wordmark" style="left:34px; top:36px; font-size:28px;">BDN Ltd</span>
  <p class="person-name">DANIEL HARWOOD</p>
  <p class="person-role">Managing Director</p>
  <p class="address">123 Fake Street<br>Anytown, New York 12345</p>
  <ul class="contact-list">
    <li><svg width="10" height="10" viewBox="0 0 10 10"><rect width="10" height="10" rx="2.5" fill="#b8901e"/><rect x="3.5" y="2.3" width="3" height="5.4" rx="0.6" fill="none" stroke="#fff" stroke-width="0.9"/></svg>555 555 55 55</li>
    <li><svg width="10" height="10" viewBox="0 0 10 10"><rect width="10" height="10" rx="2.5" fill="#b8901e"/><rect x="2.3" y="3.6" width="5.4" height="2.8" rx="1.2" fill="#fff"/></svg>888 888 88 88</li>
    <li><svg width="10" height="10" viewBox="0 0 10 10"><rect width="10" height="10" rx="2.5" fill="#b8901e"/><rect x="2.3" y="3" width="5.4" height="4" fill="#fff"/></svg>d.harwood@bdn-ltd.com</li>
  </ul>
  <span class="mark-dot" style="left:287px; top:94px; width:60px; height:60px;"></span>
</section>

<!-- Card 7: navy front, white and gold -->
<section class="card card--navy col-left row-4 c7">
  <span class="wordmark" style="left:0; width:432px; text-align:center; top:106px; font-size:38px; color:#ffffff;">BDN Ltd</span>
</section>

<!-- Card 8: navy front, gold -->
<section class="card card--navy col-right row-4 c8">
  <span class="wordmark" style="left:0; width:432px; text-align:center; top:106px; font-size:38px; color:var(--gold);">BDN Ltd</span>
</section>

</body>
</html>
```